In Search of a FANTASTIC BUSINESS CARD REFRESH AND REDESIGN

I would like to redesign the current business card for my company.  There is a parent company, Brookfane Care Group, with 2 operating companies - Brookfane Homecare and Brookfane Senior Living.
I will include the current business card design, along with the 3 logos I would like incorporated.  The business card can be two sided.  I'm looking for something clean, professional, and a fresh new look.

Target Market(s)
Hospitals, social workers, insurance agents, family members of seniors
Industry/Entity Type
Healthcare
Contact Information for Business Card
Name, title of person, address, phone number, web address, email address
Look and feel
Each slider illustrates characteristics of the customer's brand and the style your logo design should communicate.

```html
<!DOCTYPE html>
<html lang="en">
<head>
<meta charset="utf-8">
<title>Brookfane Care Group – Business Card</title>
<link href="https://fonts.googleapis.com/css2?family=Lora:ital@1&family=Poppins:wght@300;400;600&display=swap" rel="stylesheet">
<style>
  :root {
    --backdrop: #2d2d2d;
    --card: #000000;
    --white: #ffffff;
    --teal: #4f9693;
    --pink: #fb8384;
  }
  * { margin: 0; padding: 0; box-sizing: border-box; }
  html, body {
    width: 1200px; height: 1015px; overflow: hidden;
    background: var(--backdrop);
    font-family: "Poppins", sans-serif;
  }
  .canvas { position: relative; width: 1200px; height: 1015px; }
  .card {
    position: absolute; left: 250px; width: 700px; height: 400px;
    background: var(--card); overflow: hidden;
    box-shadow: 0 12px 30px rgba(0,0,0,.45);
  }
  .card--back { top: 70px; }
  .card--front { top: 545px; }
  .card__band { position: absolute; left: 0; right: 0; bottom: 0; height: 12px; }
  .card--back .card__band { background: var(--teal); }
  .card--front .card__band { background: var(--pink); }

  .brand { position: absolute; font-weight: 600; line-height: 1.1; white-space: nowrap; }
  .brand--senior { left: 80px; top: 215px; color: var(--teal); font-size: 28px; }
  .brand--homecare { left: 380px; top: 110px; color: var(--pink); font-size: 28px; }

  .group { position: absolute; left: 440px; top: 120px; }
  .group__name { color: var(--white); font-size: 34px; font-weight: 600; line-height: 1.1; }
  .tagline {
    margin-top: 16px; color: var(--white);
    font-family: "Lora", serif; font-style: italic; font-size: 15px; line-height: 1.35;
  }

  .contact { position: absolute; left: 55px; top: 55px; color: var(--white); }
  .contact__name { font-size: 30px; font-weight: 600; line-height: 1.1; }
  .contact__title { font-size: 17px; font-weight: 400; }
  .rule { width: 90px; height: 1px; background: var(--white); margin: 22px 0 24px; }
  .contact__list { list-style: none; font-size: 17px; line-height: 1.5; }
  .contact__list li { display: flex; align-items: center; gap: 12px; }
  .contact__list svg { width: 18px; height: 18px; flex: none; }
  .address { font-size: 17px; line-height: 1.4; }
</style>
</head>
<body>
<main class="canvas">
  <section class="card card--back" aria-label="Card back">
    <p class="brand brand--senior">Brookfane Senior Living</p>
    <p class="brand brand--homecare">Brookfane Homecare</p>
    <div class="card__band"></div>
  </section>

  <section class="card card--front" aria-label="Card front">
    <div class="contact">
      <h1 class="contact__name">Marla Brookfane</h1>
      <p class="contact__title">President, CEO</p>
      <div class="rule"></div>
      <ul class="contact__list">
        <li>
          <svg viewBox="0 0 24 24" fill="none" stroke="#fff" stroke-width="2"><path d="M5 3h4l2 5-3 2a11 11 0 0 0 6 6l2-3 5 2v4a2 2 0 0 1-2 2A17 17 0 0 1 3 5a2 2 0 0 1 2-2z"/></svg>
          (808) 555-0172
        </li>
        <li>
          <svg viewBox="0 0 24 24" fill="none" stroke="#fff" stroke-width="2"><rect x="2" y="5" width="20" height="14"/><path d="M2 5l10 8 10-8"/></svg>
          marla@BrookfaneCare.com
        </li>
        <li>
          <svg viewBox="0 0 24 24" fill="none" stroke="#fff" stroke-width="2"><circle cx="12" cy="12" r="10"/><path d="M2 12h20M12 2a15 15 0 0 1 0 20M12 2a15 15 0 0 0 0 20"/></svg>
          www.BrookfaneCare.com
        </li>
      </ul>
      <div class="rule"></div>
      <p class="address">4870 Maluhia Ave.,<br>Suite 310, Kailua, HI 96734</p>
    </div>
    <div class="group">
      <p class="group__name">Brookfane<br>Care Group</p>
      <p class="tagline">Someone you can depend on...<br>Without question.</p>
    </div>
    <div class="card__band"></div>
  </section>
</main>
</body>
</html>
```